Meadowlark Counseling Partners, LLC Needs Modern Business Card Design.

We provide behavioral health services from western Kansas to eastern Kansas. There is an abundance of competition for the services we provide with our main competitor being larger and having significantly more financial resources; however, the quality of services we provide is greater and we have started to catch the attention of the State of Kansas. We had a great logo designed by ArtFolio - this will be used to build upon our brand. The logo (attached) should be used in the card development. We want something unique, modern, but also a card design that clearly states our name, contact info, provides the name and unqiue location of each clinician, etc. Rounded edges, or a unique size, just something that makes our business card stand out from others. I have also uploaded each clinician's name and their unique location and phone number.

Our idea is to have one side be black with our logo. Then, on the other side have business cards for each individual. Plus, we want one card that is "generic" with no specific clinician's name listed so that we can give clients an appointment card when they leave. Some clinicians have two locations - we're open to design and background color, but we have started going with branding colors of black, the yellow in the logo files attached, and sometimes a gray. Our new office has been decorated using this theme.

Target Market(s)

individuals and families in need of behavioral health services; potential professional referral sources; existing referral sources

Industry/Entity Type

Business

Contact Information for Business Card

I attached a Word doc that provides clinician names, credentials and location information specific to each individual.

Font styles to use
Serif

Colors
000000
fbed22
dbdbdb
9d9d9d
c3c3c3

Requirements
Must have
• 1) use of the company logo that has been attached; 2) a template that provides us space to individualize business cards for all of our clinicians; 3) should stick to the colors we are branding with: black, yellow from the logo file, maybe a gray shade and we're open to a suggestion on a shade of white.
Nice to have
• Group discussion culminated in the thought that one side would be black with just our logo - no clinician names, etc. A unique design - rounded edges, unique size, some catchy lay-out would be nice.
Should not have
• Must not be too busy. Should look "clean." The project should stick to branding colors: black, yellow (from the logo file), maybe a gray and shade of white.

```html
<!DOCTYPE html>
<html lang="en">
<head>
<meta charset="utf-8">
<title>Meadowlark Counseling Partners – Business Card</title>
<link rel="stylesheet" href="https://fonts.googleapis.com/css2?family=Lora:wght@400;500&display=swap">
<style>
  :root {
    --ink: #000000;
    --paper: #ffffff;
    --backdrop: #dbdbdb;
    --gold: #f6c21c;
    --gold-bright: #fbd322;
    --text-light: #f2f2f2;
  }
  * { margin: 0; padding: 0; box-sizing: border-box; }
  html, body {
    width: 1200px;
    height: 902px;
    overflow: hidden;
    background: var(--backdrop);
  }
  .stage {
    position: relative;
    width: 1200px;
    height: 902px;
  }
  .card {
    position: absolute;
    left: 91px;
    top: 158px;
    width: 903px;
    height: 516px;
    border-radius: 24px;
    overflow: hidden;
    background: var(--paper);
    box-shadow: 0 10px 30px rgba(0,0,0,0.18);
    font-family: "Lora", Georgia, serif;
  }
  .card-shapes {
    position: absolute;
    inset: 0;
  }
  .contact-panel {
    position: absolute;
    left: 48px;
    top: 71px;
    color: var(--text-light);
    font-size: 24px;
    line-height: 31px;
  }
  .holder-name {
    font-size: 31px;
    font-weight: 500;
    line-height: 32px;
    color: var(--gold);
  }
  .holder-title { margin-bottom: 24px; }
  .office + .office { margin-top: 29px; }
  .phone {
    display: flex;
    align-items: center;
    gap: 9px;
    margin-top: 9px;
  }
  .phone svg { width: 28px; height: 28px; flex: none; }
  .tagline { margin-top: 35px; }
  .brand {
    position: absolute;
    left: 490px;
    top: 172px;
    width: 360px;
    text-align: center;
    color: var(--gold);
  }
  .brand-dot {
    width: 72px;
    height: 72px;
    margin: 0 auto 30px;
    border-radius: 50%;
    background: var(--gold);
  }
  .brand-name {
    font-size: 21px;
    font-weight: 400;
    letter-spacing: 2px;
    line-height: 30px;
    text-transform: uppercase;
  }
</style>
</head>
<body>
<main class="stage">
  <article class="card">
    <svg class="card-shapes" width="903" height="516" viewBox="0 0 903 516" aria-hidden="true">
      <path d="M0 0 H468 Q348 258 468 516 H0 Z" fill="var(--ink)"/>
      <path d="M474 0 Q352 258 474 516 Q364 258 478 0 Z" fill="var(--gold-bright)"/>
    </svg>

    <section class="contact-panel">
      <h1 class="holder-name">Daniel R. Marsh, LP</h1>
      <p class="holder-title">President</p>

      <div class="office">
        <p>418 N. Oakley St.</p>
        <p>Fairbrook, Kansas 66010</p>
        <p class="phone">
          <svg viewBox="0 0 30 30" aria-hidden="true"><circle cx="15" cy="15" r="13" fill="none" stroke="var(--gold)" stroke-width="2"/><circle cx="15" cy="15" r="10" fill="var(--gold)"/><path d="M9 13 Q15 8 21 13 L19 15 L17 13 H13 L11 15 Z M10 21 L12 16 H18 L20 21 Z" fill="var(--ink)"/></svg>
          (555) 555-0142
        </p>
      </div>

      <div class="office">
        <p>207 W. 9th St., Ste. 110</p>
        <p>Eastwick, Kansas 66412</p>
        <p class="phone">
          <svg viewBox="0 0 30 30" aria-hidden="true"><circle cx="15" cy="15" r="13" fill="none" stroke="var(--gold)" stroke-width="2"/><circle cx="15" cy="15" r="10" fill="var(--gold)"/><path d="M9 13 Q15 8 21 13 L19 15 L17 13 H13 L11 15 Z M10 21 L12 16 H18 L20 21 Z" fill="var(--ink)"/></svg>
          (555) 555-0188
        </p>
      </div>

      <p class="tagline">“Let the light find you.”</p>
    </section>

    <section class="brand">
      <div class="brand-dot"></div>
      <p class="brand-name">Meadowlark Counseling<br>Partners, LLC</p>
    </section>
  </article>
</main>
</body>
</html>
```